Yacht Management in Miami & Ft Lauderdale (2019Q2)

I’m looking for a flyer to leave places for people to get information about my company and what services we offer.
We offer monthly management plans to ensure the vessel is ready to go at a moments notice. This can be as simple as washing once a week, or as involved as washing, waxing, detailing, provisioning, and crew services.
We also offer bespoke customizations; stereos, on board WiFi, and engineering.

Target Market(s)

Yacht and boat owners.

Font styles to use
Sans Serif

Colors
87d0c7
85cae6
85acd3
cedeed
cee9f5
cfeae6
0455a3

Requirements
Must have
• Must have simple attention grabbing, without being obnoxious.
• Prefer a 3in x 5in post card size. other size may be an option.
• Must be front and back.
Nice to have
• Languages: English, Spanish, Russian
• USA flag logo
Should not have
• Should not have a lot of text. Icons and photos are great.

```html
<!DOCTYPE html>
<html lang="en">
<head>
<meta charset="utf-8">
<title>Harbor Keepers – Postcard Front and Back</title>
<link href="https://fonts.googleapis.com/css2?family=Montserrat:wght@300;400;500;700;800&display=swap" rel="stylesheet">
<style>
  :root{
    --teal:#83d0c4;
    --ink:#111111;
    --white:#ffffff;
    --page:#eeeeee;
  }
  *{box-sizing:border-box;margin:0;padding:0}
  html,body{width:960px;height:1200px;overflow:hidden;background:var(--page)}
  body{position:relative;font-family:'Montserrat',sans-serif;color:var(--ink)}
  .postcard{position:absolute;left:93px;width:774px;height:516px;overflow:hidden;background:var(--white)}
  .postcard--front{top:50px}
  .postcard--back{top:602px}
  .postcard__shapes{position:absolute;inset:0;width:774px;height:516px}
  .abs{position:absolute}

  .brand{display:flex;flex-direction:column;align-items:center;gap:6px;font-weight:800;font-size:21px;line-height:1;letter-spacing:1px;text-align:center;color:var(--ink)}
  .brand__mark{width:36px;height:36px;border-radius:50%;background:var(--ink)}

  .headline{left:402px;top:178px;width:310px;text-align:right;color:var(--white);font-size:27px;line-height:32px;white-space:nowrap}
  .headline__light{font-weight:300;display:block}
  .headline__bold{font-weight:700;display:block}
  .services{left:422px;top:262px;width:326px;text-align:center;font-size:13.5px;line-height:18px;font-weight:400}
  .extras{left:419px;top:384px;width:322px;height:48px;border-radius:24px;background:var(--ink);color:var(--white);text-align:center;font-size:12.5px;line-height:18px;padding-top:6px;letter-spacing:-.2px;white-space:nowrap}
  .extras strong{color:var(--teal);font-weight:700;display:block}

  .contact{left:0;width:774px;display:flex;justify-content:center;align-items:center;gap:8px;font-size:18.5px;font-weight:400;white-space:nowrap}
  .contact strong{font-weight:700}
  .contact__item{display:flex;align-items:center;gap:7px}
  .contact__icon{width:24px;height:24px;flex:none}
  .contact__or{margin:0 6px}
  .postcard--front .contact{top:474px}
  .postcard--back .contact{top:474px}

  .tagline{left:29px;top:28px;width:200px;font-size:15.5px;line-height:18px;font-weight:800}
  .address{left:446px;top:33px;font-size:13.5px;line-height:17px;font-weight:400;font-style:normal}
  .stamp{left:652px;top:36px;width:92px;height:92px;border:2px solid var(--ink)}
  .write-line{left:494px;width:250px;height:1.5px;background:var(--ink)}
  .gallery-tile{width:162px;height:106px;border:1.5px solid #d9d9d9;background:linear-gradient(135deg,#7d8a90,#3e4a50)}
  .social{left:98px;font-size:14px;color:var(--white);display:flex;align-items:center;gap:6px}
  .social__box{width:14px;height:14px;background:var(--teal);border-radius:2px}
</style>
</head>
<body>

<section class="postcard postcard--front">
  <svg class="postcard__shapes" viewBox="0 0 968 645" preserveAspectRatio="none" aria-hidden="true">
    <defs>
      <linearGradient id="mist" x1="0" y1="0" x2="0" y2="1"><stop offset="0" stop-color="#f7f8f8"/><stop offset="1" stop-color="#dfe4e6"/></linearGradient>
      <linearGradient id="sea" x1="0" y1="0" x2="0" y2="1"><stop offset="0" stop-color="#6a9ea3"/><stop offset="1" stop-color="#2c6670"/></linearGradient>
      <linearGradient id="panel" x1="0" y1="0" x2="1" y2="1"><stop offset="0" stop-color="#6b3b3b"/><stop offset="1" stop-color="#1e2a24"/></linearGradient>
    </defs>
    <rect width="968" height="645" fill="url(#mist)"/>
    <path d="M0 0 H385 C470 80 455 300 450 420 C448 500 470 560 480 600 H0Z" fill="var(--teal)"/>
    <path d="M0 0 H360 C440 80 440 300 430 420 C425 500 440 560 450 600 H0Z" fill="url(#sea)"/>
    <rect x="540" y="210" width="428" height="95" fill="var(--teal)"/>
    <circle cx="407" cy="495" r="75" fill="url(#panel)" stroke="var(--ink)" stroke-width="6"/>
    <path d="M0 572 C300 556 720 600 968 535 V645 H0Z" fill="var(--ink)"/>
    <path d="M0 580 C300 566 720 610 968 548 V645 H0Z" fill="var(--teal)"/>
  </svg>
  <div class="abs" role="img" aria-label="Aerial photo of a motor yacht on turquoise water" style="left:0;top:0;width:340px;height:460px"></div>
  <div class="abs" role="img" aria-label="Close-up photo of onboard electrical panel" style="left:266px;top:336px;width:120px;height:120px;border-radius:50%"></div>

  <div class="brand abs" style="left:485px;top:30px;width:200px"><span class="brand__mark"></span><span>HARBOR<br>KEEPERS</span></div>

  <h1 class="headline abs"><span class="headline__light">FAIR &amp; FRIENDLY</span><span class="headline__bold">YACHT SERVICE</span></h1>

  <p class="services abs">We offer monthly management plans to ensure the vessel is ready to go at a moments notice. This can be as simple as washing once a week, or as involved as washing, waxing, detailing, provisioning, and crew services.</p>

  <p class="extras abs">We also offer bespoke customizations;<strong>Stereos, On board WiFi, and Engineering.</strong></p>

  <div class="contact abs">
    <span class="contact__item"><svg class="contact__icon" viewBox="0 0 28 28" aria-hidden="true"><circle cx="14" cy="14" r="14" fill="var(--ink)"/><path d="M9 7.5 L11.8 7 L13 10.5 L11.3 12 C12.2 14 13.8 15.7 16 16.7 L17.5 15 L21 16.2 L20.5 19 C15 19.5 8.5 13 9 7.5Z" fill="var(--white)"/></svg>Call us <strong>(954) 555-0182</strong></span>
    <span class="contact__or">or</span>
    <span class="contact__item"><svg class="contact__icon" viewBox="0 0 28 28" aria-hidden="true"><circle cx="14" cy="14" r="14" fill="var(--ink)"/><rect x="7" y="9" width="14" height="10" fill="none" stroke="var(--white)" stroke-width="1.6"/><path d="M7 9 L14 15 L21 9" fill="none" stroke="var(--white)" stroke-width="1.6"/></svg>Email us <strong>hello@harborkeepers.us</strong></span>
  </div>
</section>

<section class="postcard postcard--back">
  <svg class="postcard__shapes" viewBox="0 0 968 645" preserveAspectRatio="none" aria-hidden="true">
    <defs>
      <linearGradient id="dusk" x1="0" y1="0" x2="1" y2="1"><stop offset="0" stop-color="#5d6b70"/><stop offset="1" stop-color="#2f3c42"/></linearGradient>
    </defs>
    <path d="M460 0 H492 C580 90 600 320 505 550 L478 550 C565 320 545 90 460 0Z" fill="var(--teal)"/>
    <path d="M0 175 H512 C548 280 545 420 478 552 L0 552Z" fill="url(#dusk)"/>
    <path d="M0 540 C260 578 620 560 968 515 V645 H0Z" fill="var(--ink)"/>
    <path d="M0 550 C260 588 620 572 968 528 V645 H0Z" fill="var(--teal)"/>
  </svg>
  <div class="abs" role="img" aria-label="Photo of a waterfront at dusk with palm trees" style="left:0;top:140px;width:400px;height:300px"></div>

  <p class="tagline abs">We perform most projects in-house, but when we use sub-contractors, we only use the best</p>

  <div class="brand abs" style="left:211px;top:18px;width:200px"><span class="brand__mark"></span><span>HARBOR<br>KEEPERS</span></div>

  <address class="address abs">2740 Coral Way,<br>#410 Miami Beach,<br>FL 33140</address>
  <div class="stamp abs"></div>
  <div class="write-line abs" style="top:280px"></div>
  <div class="write-line abs" style="top:328px"></div>
  <div class="write-line abs" style="top:376px"></div>

  <div class="gallery-tile abs" role="img" aria-label="Photo of a yellow boat cockpit" style="left:27px;top:158px"></div>
  <div class="gallery-tile abs" role="img" aria-label="Photo of a yacht hull with fenders at the dock" style="left:202px;top:158px"></div>
  <div class="gallery-tile abs" role="img" aria-label="Photo of a yacht lifted in a travel hoist" style="left:27px;top:276px"></div>
  <div class="gallery-tile abs" role="img" aria-label="Photo of a yacht cruising with wake" style="left:202px;top:276px;background:linear-gradient(135deg,#d8c6a8,#5b6c75)"></div>

  <p class="social abs" style="top:400px"><span class="social__box"></span>social.example/harborkeepers</p>
  <p class="social abs" style="top:424px"><span class="social__box"></span>photos.example/harborkeepers</p>

  <div class="contact abs">
    <span class="contact__item"><svg class="contact__icon" viewBox="0 0 28 28" aria-hidden="true"><circle cx="14" cy="14" r="14" fill="var(--ink)"/><path d="M9 7.5 L11.8 7 L13 10.5 L11.3 12 C12.2 14 13.8 15.7 16 16.7 L17.5 15 L21 16.2 L20.5 19 C15 19.5 8.5 13 9 7.5Z" fill="var(--white)"/></svg>Call us <strong>(954) 555-0182</strong></span>
    <span class="contact__or">or</span>
    <span class="contact__item"><svg class="contact__icon" viewBox="0 0 28 28" aria-hidden="true"><circle cx="14" cy="14" r="14" fill="var(--ink)"/><rect x="7" y="9" width="14" height="10" fill="none" stroke="var(--white)" stroke-width="1.6"/><path d="M7 9 L14 15 L21 9" fill="none" stroke="var(--white)" stroke-width="1.6"/></svg>Email us <strong>hello@harborkeepers.us</strong></span>
  </div>
</section>

</body>
</html>
```